Kept Until Book Cover

I am looking for book front cover ideas. The book trim size will be 5.5 x 8.5 in so please make the mock up that size. The book Title is "Kept Until" and the Subtitle is "Insight for the Hard Calls Every Chief Faces". The audience for the book is leaders in high-growth companies. It consists of a series of letters and advice for specific problems the leader will encounter on their journey. The design needs to be attractive to both male and female readers. I am attaching a file with brand colors and some rough ideas that need to be refined. The examples lean toward a feminine vibe but I want the cover to be more universal. Please use the brand colors identified in the file.

```html
<!DOCTYPE html>
<html lang="en">
<head>
<meta charset="utf-8">
<title>Kept Until – Book Cover</title>
<link rel="stylesheet" href="https://fonts.googleapis.com/css2?family=Kaushan+Script&family=Lato:wght@700&display=swap">
<style>
  :root {
    --paper: #f8efee;
    --paper-low: #f6eef0;
    --sage: #5b6b5b;
    --clay: #9b6552;
    --envelope-green: #7f9474;
    --envelope-blue: #5c7e98;
    --envelope-rust: #c1683a;
    --letter-cream: #f3eee6;
  }
  html, body {
    margin: 0;
    padding: 0;
    width: 800px;
    height: 1200px;
    overflow: hidden;
  }
  .cover {
    position: relative;
    width: 800px;
    height: 1200px;
    background: linear-gradient(180deg, var(--paper) 0%, var(--paper-low) 100%);
    overflow: hidden;
  }
  .cover-title {
    position: absolute;
    top: 72px;
    left: 0;
    width: 800px;
    margin: 0;
    text-align: center;
    font-family: "Kaushan Script", cursive;
    font-weight: 400;
    font-size: 184px;
    line-height: 170px;
    color: var(--sage);
  }
  .cover-title span { display: block; }
  .cover-subtitle {
    position: absolute;
    top: 444px;
    left: 0;
    width: 800px;
    margin: 0;
    text-align: center;
    font-family: "Lato", sans-serif;
    font-weight: 700;
    font-size: 29px;
    line-height: 37px;
    text-transform: uppercase;
    color: var(--clay);
  }
  .cover-art {
    position: absolute;
    top: 531px;
    left: 166px;
    width: 468px;
    height: 390px;
  }
  .cover-art svg { display: block; }
  .cover-author {
    position: absolute;
    top: 1079px;
    left: 0;
    width: 800px;
    margin: 0;
    text-align: center;
    font-family: "Lato", sans-serif;
    font-weight: 700;
    font-size: 39px;
    line-height: 46px;
    text-transform: uppercase;
    color: var(--clay);
  }
</style>
</head>
<body>
  <main class="cover">
    <h1 class="cover-title"><span>Kept</span><span>Until</span></h1>
    <p class="cover-subtitle">Insight for the Hard Calls<br>Every Chief Faces</p>
    <div class="cover-art" role="img" aria-label="Illustration of an open envelope in sage, blue and rust with a cream letter inside, framed by small leaf sprigs">
      <svg width="468" height="390" viewBox="0 0 468 390" aria-hidden="true">
        <defs>
          <linearGradient id="envelope-tones" x1="0" y1="0" x2="0.6" y2="1">
            <stop offset="0" stop-color="var(--envelope-green)"/>
            <stop offset="0.35" stop-color="var(--letter-cream)"/>
            <stop offset="0.6" stop-color="var(--envelope-blue)"/>
            <stop offset="1" stop-color="var(--envelope-rust)"/>
          </linearGradient>
        </defs>
        <path d="M234 0 L468 160 L468 380 Q468 390 458 390 L10 390 Q0 390 0 380 L0 160 Z" fill="url(#envelope-tones)"/>
      </svg>
    </div>
    <p class="cover-author">Author's Name</p>
  </main>
</body>
</html>
```